Fernbrook Yield - Online-only garden installation company

Online-only garden installation company. Our demographic is middle aged / suburban women, and we anticipate Facebook driving traffic to this website, as well as referrals from garden centers. The website must be very simple in design and function.

All orders will be placed through the website, including size of garden (3 options), location in yard, payment, and scheduling of installation date.

The website should employ a 3 step process:

Step 1: Select garden size. Either an 4' X 4', 8' X 4', or 12' X 4'.

Step 2: Select a location. We would like to use google maps to look up a US address, then "drag and drop" one of the garden sizes from step 1 to the location the customer would like us to install the garden at their home.

Step 3: Pick an installation date and pay. Using an online calendar the customer will pick a date, and then pay for the installation via credit card.

The website will be linked to an email account, FernbrookYield@mailvista.example to inform us of orders placed.

Target Market(s)

Our demographic is middle aged / suburban women, and we anticipate Facebook driving traffic to this website, as well as referrals from garden centers.

Industry/Entity Type

It Company

Coding

Coded - Design and coding required

Number of Pages Required

4 page

Requirements
Must have
• Scheduling and payment options.

```html
<!DOCTYPE html>
<html lang="en">
<head>
<meta charset="utf-8">
<title>Fernbrook Yield – Garden Installation</title>
<link href="https://fonts.googleapis.com/css2?family=Lato:wght@400;700;900&family=Open+Sans:wght@400;600;700&family=Great+Vibes&display=swap" rel="stylesheet">
<style>
:root{
  --green:#1c9a4a;
  --green-dark:#15803c;
  --green-pale:#e6f5ea;
  --green-pale-2:#f1faf3;
  --charcoal:#3b3b3b;
  --charcoal-deep:#2e2e2e;
  --beige:#e4ddcc;
  --olive:#8c7a35;
  --ink:#333;
  --muted:#666;
  --white:#fff;
}
*{box-sizing:border-box;margin:0;padding:0}
html,body{width:1200px;height:3297px;overflow:hidden}
body{position:relative;font-family:"Open Sans",Arial,sans-serif;color:var(--ink);background:var(--white)}
.abs{position:absolute}

/* header */
.topbar{left:0;top:0;width:1200px;height:105px;background:var(--charcoal)}
.logo-box{left:121px;top:0;width:187px;height:167px;background:var(--white);z-index:5;display:flex;flex-direction:column;align-items:center;justify-content:center;gap:10px}
.logo-mark{width:22px;height:22px;border-radius:50%;background:var(--green)}
.logo-name{font-family:"Lato",sans-serif;font-weight:900;font-size:19px;line-height:1.15;color:var(--charcoal);text-align:center;letter-spacing:1px}
.top-phone{left:734px;top:18px;display:flex;align-items:center;gap:8px;color:#ddd;font:600 13px "Open Sans",sans-serif}
.icon-circle{width:22px;height:22px;border-radius:50%;border:2px solid var(--green);display:flex;align-items:center;justify-content:center}
.quote-btn{left:934px;top:15px;width:136px;height:27px;border:2px solid var(--green);color:var(--green);font:700 11px "Lato",sans-serif;letter-spacing:1px;display:flex;align-items:center;justify-content:center;gap:8px}
.follow{left:880px;top:63px;display:flex;align-items:center;gap:6px;color:#ddd;font:700 12px "Lato",sans-serif;letter-spacing:1px}
.social{width:22px;height:22px;border-radius:50%;border:1.5px solid #ddd}
.nav{left:308px;top:105px;width:892px;height:60px;background:var(--green);display:flex;align-items:center;padding-left:62px}
.nav a{color:var(--white);text-decoration:none;font:700 14px "Lato",sans-serif;letter-spacing:1px;padding:0 30px;height:60px;display:flex;align-items:center;border-right:1px solid rgba(255,255,255,.35)}
.nav a:last-child{border-right:none}

/* hero */
.hero{left:0;top:165px;width:1200px;height:479px;background:linear-gradient(180deg,#8fb0c8 0%,#6f8f6e 35%,#4f8a36 60%,#3f7d2a 100%)}
.hero-card{left:396px;top:301px;width:329px;height:215px;background:rgba(255,255,255,.88);border:3px solid var(--white);outline:2px solid var(--green);outline-offset:-10px;text-align:center;padding-top:22px}
.hero-card .lead{font:900 25px "Lato",sans-serif;color:var(--charcoal);letter-spacing:1px;line-height:1.1}
.hero-card .script{font:400 48px "Great Vibes",cursive;color:var(--green);line-height:1.1}
.hero-btn{display:inline-flex;align-items:center;gap:8px;margin-top:10px;background:var(--green);color:var(--white);font:700 15px "Lato",sans-serif;letter-spacing:1px;padding:8px 16px}
.dots{left:548px;top:610px;display:flex;gap:10px}
.dots span{width:16px;height:16px;border-radius:50%;background:var(--green-dark)}
.dots span:first-child{background:var(--green)}

/* services */
.services{left:0;top:644px;width:1200px;height:402px;background:var(--green-pale)}
.service{top:644px;width:238px;height:402px;text-align:center;padding-top:37px}
.service.alt{background:var(--green-pale-2)}
.service .thumb{width:126px;height:126px;border-radius:50%;margin:0 auto;border:5px solid var(--white);box-shadow:0 0 0 1px #cfd9cf}
.service h3{font:900 19px "Lato",sans-serif;letter-spacing:1px;color:var(--charcoal);margin-top:30px}
.leaf-rule{display:flex;align-items:center;justify-content:center;gap:6px;margin:10px auto 0;width:160px}
.leaf-rule i{flex:1;height:1px;background:var(--green)}
.leaf-rule b{width:10px;height:10px;background:var(--green);border-radius:0 8px 0 8px}
.service p{font-size:13px;line-height:19px;color:var(--muted);width:205px;margin:14px auto 0}
.read-more{display:inline-flex;align-items:center;gap:8px;margin-top:14px;border:2px solid var(--charcoal);padding:3px 10px;font:900 11px "Lato",sans-serif;letter-spacing:1px;color:var(--charcoal)}

/* welcome */
.grass{left:0;top:1046px;width:1200px;height:440px;background:linear-gradient(180deg,#3f8e2c 0%,#55a83a 50%,#4c9a33 100%)}
.welcome{left:125px;top:1121px;width:945px;height:242px;background:rgba(28,154,74,.92);border:1px dashed rgba(255,255,255,.7);outline:6px solid rgba(28,154,74,.92);text-align:center;color:var(--white);padding:22px 40px 0}
.welcome h2{font:700 25px "Lato",sans-serif;letter-spacing:1px}
.welcome .leaf-rule i{background:rgba(255,255,255,.6)}
.welcome .leaf-rule b{background:var(--white)}
.welcome p{font-size:12.5px;line-height:23px;margin:12px auto 0;max-width:820px}
.stones{left:0;top:1400px;width:1200px;height:130px;background:linear-gradient(180deg,rgba(160,160,150,0) 0%,#b8b4a6 35%,#a9a496 60%,var(--beige) 100%)}

/* projects */
.projects{left:0;top:1520px;width:1200px;height:399px;background:var(--beige)}
.section-title{font:900 25px "Lato",sans-serif;color:var(--olive);text-align:center;letter-spacing:1px}
.projects-title{left:0;top:1553px;width:1200px}
.proj{top:1675px;width:176px;height:171px;border:4px solid var(--white)}
.proj-featured{left:503px;top:1648px;width:185px;height:216px;background:var(--white);text-align:center;padding-top:8px}
.proj-featured .date{font:600 14px "Open Sans",sans-serif;color:var(--ink)}
.proj-featured .img{width:167px;height:140px;margin:6px auto 0}
.proj-featured .meta{font:700 13px "Open Sans",sans-serif;margin-top:8px;display:flex;justify-content:center;gap:14px}
.arrow-btn{top:1738px;width:32px;height:34px;border:2px solid #6b6b5a;display:flex;align-items:center;justify-content:center;background:var(--beige)}

/* steps */
.steps-bg{left:0;top:1919px;width:1200px;height:620px;background:linear-gradient(90deg,#3f6b3a 0%,#6a8a5a 30%,#5f7f48 70%,#3b6430 100%)}
.steps-head{left:95px;top:1963px;width:1015px;height:81px;background:var(--white);border-radius:14px 14px 0 0;padding-top:16px}
.steps-head .section-title{font:900 24px "Lato",sans-serif;color:var(--charcoal)}
.steps-panel{left:95px;top:2044px;width:1015px;height:451px;background:var(--green)}
.label{font:700 18px "Lato",sans-serif;color:var(--white)}
.field{height:49px;background:#e9e6dc;border:1px solid #cfcab8;font-size:13px;color:#888;display:flex;align-items:center;padding-left:14px}
.field-btn{background:var(--green-dark);display:flex;align-items:center;justify-content:center}
.white-btn{background:var(--white);color:var(--green);font:700 14px "Lato",sans-serif;display:flex;align-items:center;justify-content:center;border-radius:2px}
.calendar{left:475px;top:2224px;width:132px;height:123px;background:var(--white);font-size:7.5px;color:var(--ink);padding:3px}
.calendar .cal-head{display:flex;justify-content:space-between;font-weight:700;padding:1px 3px 3px}
.calendar table{width:100%;border-collapse:collapse;text-align:center}
.calendar td,.calendar th{padding:1px 0;line-height:11px}
.calendar th{font-weight:700}
.calendar td.sel{background:#2a6dcc;color:var(--white)}
.calendar td.dim{color:#bbb}
.map{left:624px;top:2071px;width:449px;height:384px;background:linear-gradient(135deg,#e9e7e1 0%,#dedbd2 50%,#e7e4dc 100%);border:1px solid #ccc}
.pay-row{left:119px;top:2368px;display:flex;align-items:center;gap:6px}
.radio{width:14px;height:14px;border-radius:50%;background:var(--white);border:2px solid var(--white);box-shadow:inset 0 0 0 3px var(--white)}
.radio.on{background:var(--green-dark)}
.card{width:46px;height:26px;background:var(--white);border-radius:3px;font:700 9px "Open Sans",sans-serif;color:var(--charcoal);display:flex;align-items:center;justify-content:center}

/* tips */
.tips-title{left:189px;top:2580px;font:900 21px "Lato",sans-serif;color:var(--charcoal);letter-spacing:.5px}
.tips-title span{color:var(--green)}
.tip{left:191px;width:480px;display:flex;gap:18px}
.tip .img{width:128px;height:80px;flex:none}
.tip h4{font:700 13px "Open Sans",sans-serif;color:var(--green)}
.tip .date{font:700 12px "Open Sans",sans-serif;color:var(--ink);margin:3px 0 2px}
.tip p{font-size:11.5px;line-height:17px;color:var(--muted)}
.tip p a{color:var(--green);font-weight:700;text-decoration:none}
.newsletter{left:734px;top:2600px;width:279px;height:209px;background:var(--green);text-align:center;padding:12px}
.newsletter .frame{border:2px solid var(--white);height:100%;padding-top:18px}
.newsletter h3{font:700 18px "Lato",sans-serif;color:var(--white)}
.newsletter .leaf-rule{width:80px}
.newsletter .leaf-rule i{background:rgba(255,255,255,.7)}
.newsletter .leaf-rule b{background:var(--white)}
.newsletter .input{width:233px;height:22px;background:var(--white);margin:14px auto 0;text-align:left;padding-left:8px;font-size:11px;color:#888;line-height:22px}
.newsletter .input+.input{margin-top:8px}
.submit{display:inline-flex;align-items:center;gap:5px;margin-top:16px;background:var(--green-dark);border:2px solid var(--white);border-radius:14px;padding:2px 12px;font:900 11px "Lato",sans-serif;color:var(--white);letter-spacing:1px}

.silhouette{left:0;top:2835px;width:1200px;height:159px;background:linear-gradient(180deg,#ffffff 0%,#dfe8f0 45%,#9aa6ae 80%,#3b3b3b 100%)}

/* footer */
.footer{left:0;top:2994px;width:1200px;height:263px;background:var(--charcoal)}
.foot-col{top:3036px;color:#e6e6e6}
.foot-col h5{font:700 15px "Lato",sans-serif;letter-spacing:1px;color:var(--white);margin-bottom:18px}
.foot-col li{list-style:none;font:700 14px "Lato",sans-serif;line-height:28px}
.foot-col li::before{content:"›";margin-right:8px;font-weight:900}
.contact-line{display:flex;gap:10px;font:700 14px "Lato",sans-serif;line-height:22px;margin-bottom:12px}
.foot-logo{left:884px;top:3038px;width:189px;height:167px;background:#9a9a9a;display:flex;flex-direction:column;align-items:center;justify-content:center;gap:10px}
.foot-logo .logo-name{color:var(--charcoal)}
.bottombar{left:0;top:3257px;width:1200px;height:40px;background:var(--charcoal-deep);color:#ddd;font:700 12px "Lato",sans-serif;letter-spacing:.5px}
.bottombar .copy{position:absolute;left:121px;top:13px}
.bottombar .links{position:absolute;left:460px;top:13px}
.bottombar .links span{padding:0 12px;border-left:1px solid #aaa}
.bottombar .links span:first-child{border-left:none;padding-left:0}
.bottombar .socials{position:absolute;left:968px;top:9px;display:flex;gap:6px}
.bottombar .social{width:20px;height:20px}
</style>
</head>
<body>

<!-- header -->
<div class="abs topbar"></div>
<div class="abs logo-box">
  <span class="logo-mark"></span>
  <div class="logo-name">FERNBROOK<br>YIELD</div>
</div>
<div class="abs top-phone">
  <span class="icon-circle"><svg width="11" height="11" viewBox="0 0 24 24"><path fill="#1c9a4a" d="M6.6 10.8a15 15 0 0 0 6.6 6.6l2.2-2.2a1 1 0 0 1 1-.25 11.4 11.4 0 0 0 3.6.57 1 1 0 0 1 1 1V20a1 1 0 0 1-1 1A17 17 0 0 1 3 4a1 1 0 0 1 1-1h3.5a1 1 0 0 1 1 1c0 1.250.2 2.45.57 3.57a1 1 0 0 1-.25 1z"/></svg></span>
  Call: 123-456-7890
</div>
<div class="abs quote-btn">GET A QUOTE
  <svg width="14" height="14" viewBox="0 0 14 14"><circle cx="7" cy="7" r="7" fill="#1c9a4a"/><path d="M5.5 4l3 3-3 3" stroke="#3b3b3b" stroke-width="1.8" fill="none"/></svg>
</div>
<div class="abs follow">FOLLOW US:
  <span class="social" aria-label="Social profile"></span>
  <span class="social" aria-label="Social profile"></span>
  <span class="social" aria-label="Social profile"></span>
  <span class="social" aria-label="Social profile"></span>
</div>
<nav class="abs nav">
  <a href="#">HOME</a><a href="#">ABOUT US</a><a href="#">SERVICES</a><a href="#">CONTACT US</a>
</nav>

<!-- hero -->
<div class="abs hero" role="img" aria-label="Photo of a smiling gardener standing on a green lawn in front of a suburban house"></div>
<div class="abs hero-card">
  <div class="lead">MORE THAN<br>30 YEARS</div>
  <div class="script">Experience</div>
  <div class="hero-btn">GET A QUOTE
    <svg width="12" height="12" viewBox="0 0 12 12"><circle cx="6" cy="6" r="6" fill="#fff"/><path d="M5 3.5l2.5 2.5L5 8.5" stroke="#1c9a4a" stroke-width="1.6" fill="none"/></svg>
  </div>
</div>
<div class="abs dots"><span></span><span></span><span></span><span></span></div>

<!-- services -->
<div class="abs services"></div>
<div class="abs service alt" style="left:121px">
  <div class="thumb" role="img" aria-label="Stepping stone path across a lawn" style="background:radial-gradient(circle,#9a9a88 0%,#5e8a3a 60%,#3d6b26 100%)"></div>
  <h3>LANDSCAPES</h3>
  <div class="leaf-rule"><i></i><b></b><i></i></div>
  <p>Lorem Ipsum has been the industry's standard dummy text ever since the 1500s,when an unknown printer took</p>
  <div class="read-more">READ MORE <svg width="12" height="12" viewBox="0 0 12 12"><circle cx="6" cy="6" r="6" fill="#3b3b3b"/><path d="M5 3.5l2.5 2.5L5 8.5" stroke="#fff" stroke-width="1.6" fill="none"/></svg></div>
</div>
<div class="abs service" style="left:358px">
  <div class="thumb" role="img" aria-label="Garden pond with rocks" style="background:radial-gradient(circle,#6f6a5a 0%,#8a6e4e 55%,#4f6a34 100%)"></div>
  <h3>WATERSCAPES</h3>
  <div class="leaf-rule"><i></i><b></b><i></i></div>
  <p>Lorem Ipsum has been the industry's standard dummy text ever since the 1500s,when an unknown printer took</p>
  <div class="read-more">READ MORE <svg width="12" height="12" viewBox="0 0 12 12"><circle cx="6" cy="6" r="6" fill="#3b3b3b"/><path d="M5 3.5l2.5 2.5L5 8.5" stroke="#fff" stroke-width="1.6" fill="none"/></svg></div>
</div>
<div class="abs service alt" style="left:598px">
  <div class="thumb" role="img" aria-label="Stone patio with a fire pit" style="background:radial-gradient(circle,#c46a2a 0%,#8a7560 45%,#4e6a3a 100%)"></div>
  <h3>LIFESCAPES</h3>
  <div class="leaf-rule"><i></i><b></b><i></i></div>
  <p>Lorem Ipsum has been the industry's standard dummy text ever since the 1500s,when an unknown printer took</p>
  <div class="read-more">READ MORE <svg width="12" height="12" viewBox="0 0 12 12"><circle cx="6" cy="6" r="6" fill="#3b3b3b"/><path d="M5 3.5l2.5 2.5L5 8.5" stroke="#fff" stroke-width="1.6" fill="none"/></svg></div>
</div>
<div class="abs service" style="left:835px">
  <div class="thumb" role="img" aria-label="Gardener mowing a lawn" style="background:radial-gradient(circle,#5a5a4a 0%,#5e8a3a 55%,#3f6e28 100%)"></div>
  <h3>MAINTENANCE</h3>
  <div class="leaf-rule"><i></i><b></b><i></i></div>
  <p>Lorem Ipsum has been the industry's standard dummy text ever since the 1500s,when an unknown printer took</p>
  <div class="read-more">READ MORE <svg width="12" height="12" viewBox="0 0 12 12"><circle cx="6" cy="6" r="6" fill="#3b3b3b"/><path d="M5 3.5l2.5 2.5L5 8.5" stroke="#fff" stroke-width="1.6" fill="none"/></svg></div>
</div>

<!-- welcome -->
<div class="abs grass" role="img" aria-label="Close-up of a green lawn"></div>
<div class="abs stones" role="img" aria-label="Curving border of river stones"></div>
<div class="abs welcome">
  <h2>WELCOME TO FERNBROOK YIELD</h2>
  <div class="leaf-rule"><i></i><b></b><i></i></div>
  <p>Lorem Ipsum has been the industry's standard dummy text ever since the 1500s, when an unknown printer took a galley of type and scrambled it to make a type specimen book. It has survived not only five centuries, but also the leap into electronic typesetting, remaining essentially unchanged. It was popularised in the 1960s with the release of Lettrafax sheets containing Lorem Ipsum passages, and more recently with desktop publishing software like Pagewright Studio including versions of Lorem Ipsum.</p>
</div>

<!-- recent projects -->
<div class="abs projects"></div>
<div class="abs projects-title section-title">RECENT PROJECTS
  <div class="leaf-rule" style="width:90px;margin-top:6px"><i style="background:var(--olive)"></i><b></b><i style="background:var(--olive)"></i></div>
</div>
<div class="abs arrow-btn" style="left:67px"><svg width="10" height="12" viewBox="0 0 10 12"><path d="M7 1L2 6l5 5" stroke="#555" stroke-width="2" fill="none"/></svg></div>
<div class="abs arrow-btn" style="left:1087px"><svg width="10" height="12" viewBox="0 0 10 12"><path d="M3 1l5 5-5 5" stroke="#555" stroke-width="2" fill="none"/></svg></div>
<div class="abs proj" style="left:117px;background:linear-gradient(160deg,#7a5a3e,#5d7a3a)" role="img" aria-label="Raised wooden garden beds"></div>
<div class="abs proj" style="left:315px;background:linear-gradient(160deg,#8a6a50,#6a6a52)" role="img" aria-label="Stone patio garden"></div>
<div class="abs proj-featured">
  <div class="date">01 Febuary 2016</div>
  <div class="img" style="background:linear-gradient(160deg,#4f8a2e,#c9a540 60%,#3f7a2a)" role="img" aria-label="Garden path lined with flowers"></div>
  <div class="meta"><span>♥ 414</span><span>● 21</span></div>
</div>
<div class="abs proj" style="left:710px;background:linear-gradient(160deg,#7a6a55,#5a7a3a)" role="img" aria-label="Vegetable beds in a backyard"></div>
<div class="abs proj" style="left:898px;background:linear-gradient(160deg,#5a8a3a,#b84a3a 55%,#4f7a2e)" role="img" aria-label="Green living wall with red plants"></div>

<!-- 3 step process -->
<div class="abs steps-bg" role="img" aria-label="Lush garden with stone path and statues"></div>
<div class="abs steps-head"><div class="section-title">3 STEP PROCESS</div>
  <div class="leaf-rule" style="width:90px;margin-top:6px"><i></i><b></b><i></i></div>
</div>
<div class="abs steps-panel"></div>
<div class="abs label" style="left:119px;top:2066px">Select garden size</div>
<div class="abs field" style="left:119px;top:2105px;width:343px">Either an 4' X 4', 8' X 4', or 12' X 4'</div>
<div class="abs field-btn" style="left:422px;top:2110px;width:36px;height:38px"><svg width="12" height="8" viewBox="0 0 12 8"><path d="M1 1l5 5 5-5" stroke="#fff" stroke-width="2" fill="none"/></svg></div>
<div class="abs white-btn" style="left:475px;top:2105px;width:127px;height:49px">Add In Map</div>
<div class="abs label" style="left:119px;top:2187px">Select Date</div>
<div class="abs field" style="left:119px;top:2229px;width:343px;color:#777">12-02-2016</div>
<div class="abs" style="left:410px;top:2229px;width:52px;height:49px;background:#dcd8cb;display:flex;align-items:center;justify-content:center"><svg width="16" height="16" viewBox="0 0 16 16"><rect x="1" y="2" width="14" height="13" fill="none" stroke="#555" stroke-width="1.5"/><rect x="1" y="2" width="14" height="3" fill="#555"/><path d="M4 8h2M8 8h2M12 8h1M4 11h2M8 11h2" stroke="#555" stroke-width="1.5"/></svg></div>
<div class="abs calendar">
  <div class="cal-head"><span>‹</span><span>February 2016</span><span>›</span></div>
  <table>
    <tr><th>Su</th><th>Mo</th><th>Tu</th><th>We</th><th>Th</th><th>Fr</th><th>Sa</th></tr>
    <tr><td class="dim">31</td><td>1</td><td>2</td><td>3</td><td>4</td><td>5</td><td>6</td></tr>
    <tr><td>7</td><td>8</td><td>9</td><td>10</td><td>11</td><td class="sel">12</td><td>13</td></tr>
    <tr><td>14</td><td>15</td><td>16</td><td>17</td><td>18</td><td>19</td><td>20</td></tr>
    <tr><td>21</td><td>22</td><td>23</td><td>24</td><td>25</td><td>26</td><td>27</td></tr>
    <tr><td>28</td><td>29</td><td class="dim">1</td><td class="dim">2</td><td class="dim">3</td><td class="dim">4</td><td class="dim">5</td></tr>
  </table>
</div>
<div class="abs label" style="left:119px;top:2318px">Secure Payment</div>
<div class="abs pay-row">
  <span class="radio on"></span>
  <span class="card">Cardia</span><span class="card">Vantis</span><span class="card">Amplo</span><span class="card">Dispay</span>
  <span class="radio" style="margin-left:16px"></span>
  <span class="card">Paywell</span>
</div>
<div class="abs white-btn" style="left:119px;top:2422px;width:176px;height:35px;border-radius:6px;font-size:15px">Pay $72.40</div>
<div class="abs map" role="img" aria-label="Street map with a pin marking the customer's address"></div>
<svg class="abs" style="left:830px;top:2220px" width="22" height="32" viewBox="0 0 22 32"><path d="M11 0a11 11 0 0 1 11 11c0 8-11 21-11 21S0 19 0 11A11 11 0 0 1 11 0z" fill="#d93a2e"/><circle cx="11" cy="11" r="4" fill="#8a1f18"/></svg>

<!-- gardening tips -->
<div class="abs tips-title"><span>GARDENING</span> TIPS</div>
<div class="abs tip" style="top:2620px">
  <div class="img" style="background:linear-gradient(160deg,#7fbf4a,#4f9a2e)" role="img" aria-label="Fresh green lawn"></div>
  <div>
    <h4>Lorem Ipsum has been the industry's standard.</h4>
    <div class="date">Feb 24 2017</div>
    <p>Lorem Ipsum has been the industry's standard dummy text ever since the 1500s, when an unknown printer took a galley of type and scrambled. <a href="#">Read More</a></p>
  </div>
</div>
<div class="abs tip" style="top:2726px">
  <div class="img" style="background:linear-gradient(160deg,#a89a7a,#5f8a3a)" role="img" aria-label="Garden tools and potted plants"></div>
  <div>
    <h4>Lorem Ipsum has been the industry's standard.</h4>
    <div class="date">Feb 24 2017</div>
    <p>Lorem Ipsum has been the industry's standard dummy text ever since the 1500s, when an unknown printer took a galley of type and scrambled. <a href="#">Read More</a></p>
  </div>
</div>
<div class="abs newsletter">
  <div class="frame">
    <h3>Subcribe Newsletter</h3>
    <div class="leaf-rule"><i></i><b></b><i></i></div>
    <div class="input">Name</div>
    <div class="input">Email Address</div>
    <div class="submit">SUBMIT <svg width="10" height="10" viewBox="0 0 10 10"><circle cx="5" cy="5" r="5" fill="#fff"/><path d="M4 2.8L6.2 5 4 7.2" stroke="#15803c" stroke-width="1.5" fill="none"/></svg></div>
  </div>
</div>

<div class="abs silhouette" role="img" aria-label="Silhouette of gardeners working in a park with a fountain and bench"></div>

<!-- footer -->
<div class="abs footer"></div>
<div class="abs foot-col" style="left:121px">
  <h5>WHO WE ARE</h5>
  <ul><li>About us</li><li>Our Team</li><li>Gallery</li><li>Blog</li><li>Get a Quote</li></ul>
</div>
<div class="abs foot-col" style="left:352px">
  <h5>IMPORTANT LINKS</h5>
  <ul><li>Landscapes</li><li>Waterscaps</li><li>Lifescapes</li><li>Maintenance</li><li>Other Services</li></ul>
</div>
<div class="abs foot-col" style="left:587px">
  <h5>CONTACT US</h5>
  <div class="contact-line"><svg width="16" height="16" viewBox="0 0 16 16" style="margin-top:3px"><path d="M8 1L1 7h2v7h4v-4h2v4h4V7h2z" fill="#e6e6e6"/></svg><span>123, Office Building,<br>Street, City, Country.</span></div>
  <div class="contact-line"><svg width="16" height="16" viewBox="0 0 24 24" style="margin-top:3px"><path fill="#e6e6e6" d="M6.6 10.8a15 15 0 0 0 6.6 6.6l2.2-2.2a1 1 0 0 1 1-.25 11.4 11.4 0 0 0 3.6.57 1 1 0 0 1 1 1V20a1 1 0 0 1-1 1A17 17 0 0 1 3 4a1 1 0 0 1 1-1h3.5a1 1 0 0 1 1 1c0 1.25.2 2.45.57 3.57a1 1 0 0 1-.25 1z"/></svg><span>123-456-7890</span></div>
  <div class="contact-line"><svg width="16" height="12" viewBox="0 0 16 12" style="margin-top:5px"><rect width="16" height="12" fill="#e6e6e6"/><path d="M0 0l8 6 8-6" stroke="#3b3b3b" stroke-width="1.5" fill="none"/></svg><span>Info@yourdomain.com</span></div>
</div>
<div class="abs foot-logo">
  <span class="logo-mark"></span>
  <div class="logo-name">FERNBROOK<br>YIELD</div>
</div>
<div class="abs bottombar">
  <span class="copy">Copyright 2017. All rights reserved.</span>
  <span class="links"><span>Terms &amp; Condition</span><span>Privacy Policy</span></span>
  <span class="socials"><span class="social"></span><span class="social"></span><span class="social"></span><span class="social"></span></span>
</div>

</body>
</html>
```